Exclusive Crown Clippers Invite that connects barbers

I am looking for a general invitation to join a secret club of people that shave their head. I want it the size of a business card that I can hand out to people I see on the street. I want it to feel like a special exclulisve invite to a club that only they can be apart of and want to tell their friends about.

Target Market(s)

35-60 male

Industry/Entity Type

Hair

Contact Information for Business Card

I want it to look like an invite to a secret club that only people that shave their head can be apart of... I will hand it out to people that I think fir our demographic.

Font styles to use
Serif

Colors

Designer to choose colors to be used in the design.

Requirements
Must have
• A feel of exclusivity
• website address (www.crownclippers.example)
• logo

```html
<!DOCTYPE html>
<html lang="en">
<head>
<meta charset="utf-8">
<title>Crown Clippers – Business Card</title>
<link rel="stylesheet" href="https://fonts.googleapis.com/css2?family=Jura:wght@500;600;700&family=PT+Sans:wght@400;700&display=swap">
<style>
  :root {
    --bg: #e9e4df;
    --rose: #d99a8c;
    --rose-deep: #c9806f;
    --ink: #1e1e1e;
    --paper: #ffffff;
    --text: #2a2a2a;
  }
  * { box-sizing: border-box; margin: 0; padding: 0; }
  html, body { width: 1200px; height: 900px; overflow: hidden; }
  body {
    background: var(--bg);
    font-family: "PT Sans", sans-serif;
    position: relative;
  }
  .card {
    position: absolute;
    left: 300px;
    width: 600px;
    height: 343px;
    border-radius: 4px;
    overflow: hidden;
    box-shadow: 0 6px 18px rgba(0,0,0,0.18);
  }
  .card-front { top: 90px; background: var(--rose); }
  .card-back { top: 467px; background: var(--paper); }

  .brand {
    position: absolute;
    left: 0; right: 0; top: 88px;
    display: flex; flex-direction: column; align-items: center; gap: 26px;
  }
  .brand-square {
    width: 92px; height: 92px;
    border: 6px solid var(--ink);
    border-radius: 8px;
  }
  .brand-name {
    font-family: "Jura", sans-serif;
    font-weight: 700;
    font-size: 52px;
    color: var(--ink);
    letter-spacing: 1px;
    line-height: 1;
  }

  .back-swoosh { position: absolute; inset: 0; }
  .person { position: absolute; left: 54px; top: 84px; }
  .person-name {
    font-family: "Jura", sans-serif;
    font-weight: 600;
    font-size: 22px;
    color: var(--rose-deep);
    letter-spacing: 1px;
    text-transform: uppercase;
  }
  .person-role { font-size: 15px; color: var(--text); margin-top: 2px; }

  .contacts { position: absolute; left: 54px; top: 178px; font-size: 16px; color: var(--text); line-height: 21px; }
  .contact-line { display: flex; align-items: center; gap: 8px; }
  .contact-line svg { width: 12px; height: 12px; flex: none; }
  .address { margin-top: 6px; margin-left: 0; font-size: 16px; line-height: 22px; }

  .mark { position: absolute; right: 40px; top: 38px; display: flex; flex-direction: column; align-items: center; gap: 10px; }
  .mark-square { width: 96px; height: 96px; border: 6px solid var(--ink); border-radius: 8px; }
  .mark-name { font-family: "Jura", sans-serif; font-weight: 700; font-size: 15px; color: var(--ink); }

  .website {
    position: absolute; right: 40px; top: 240px;
    font-size: 14px; color: var(--paper);
  }
</style>
</head>
<body>
  <section class="card card-front">
    <div class="brand">
      <div class="brand-square"></div>
      <div class="brand-name">Crown Clippers</div>
    </div>
  </section>

  <section class="card card-back">
    <svg class="back-swoosh" viewBox="0 0 600 343" preserveAspectRatio="none" aria-hidden="true">
      <path d="M0 300 C 150 255, 330 250, 470 215 C 530 200, 570 185, 600 175 L600 190 C 470 230, 300 280, 0 318 Z" fill="var(--rose)"/>
      <path d="M0 318 C 200 290, 380 255, 470 225 C 530 205, 570 190, 600 180 L600 343 L0 343 Z" fill="var(--ink)"/>
    </svg>

    <div class="person">
      <div class="person-name">Marcus Hale</div>
      <div class="person-role">Managing Director</div>
    </div>

    <div class="contacts">
      <div class="contact-line">
        <svg viewBox="0 0 12 12"><path d="M1 4 Q6 0 11 4 L9 6 L8 4 Q6 3 4 4 L3 6 Z M3 7 H9 V11 H3 Z" fill="var(--rose-deep)"/></svg>
        <span>(044) 555 0142</span>
      </div>
      <div class="contact-line">
        <svg viewBox="0 0 12 12"><rect x="3" y="0.5" width="6" height="11" rx="1" fill="none" stroke="var(--rose-deep)" stroke-width="1.3"/></svg>
        <span>(044)555 0187</span>
      </div>
      <div class="contact-line">
        <svg viewBox="0 0 12 12"><rect x="0.5" y="2" width="11" height="8" fill="var(--rose-deep)"/><path d="M0.5 2 L6 7 L11.5 2" fill="none" stroke="#fff" stroke-width="1"/></svg>
        <span>info@crownclippers.example</span>
      </div>
      <div class="address">1234, Address GoesHere,<br>Country, 12345</div>
    </div>

    <div class="mark">
      <div class="mark-square"></div>
      <div class="mark-name">Crown Clippers</div>
    </div>

    <div class="website">www.crownclippers.example</div>
  </section>
</body>
</html>
```